Young Accounting firm needing a captivating business card

We need a business card design that forces the person to look at the card because its either gold foil, plastic, or lettering pop up etc. We already have a logo with a specific gold color and we need to make it pop. We are an accounting firm. I need the words" accounting, payroll, licenses, audits, taxes" somewhere on the business card so as to describe what we do- preferably on the side where the logo is at.

Industry/Entity Type

Accounting

Contact Information for Business Card

Address 48276 9th Ave S Ste 305, Federal Way, WA 98117
Business Phone (360)418-2096
Fax (360)418-2157
Office Cell Phone (360)586-7319

Font styles to use
Serif

Colors
85abd2

Requirements
Must have
• It should state
• "Accounting" "Taxes" "Audits" "Licenses" "Payroll"
Nice to have
• Matte with gold foil, different textures, With Either a textured ivory background or gray blue slate background
Should not have
• colorful colors

```html
<!DOCTYPE html>
<html lang="en">
<head>
<meta charset="utf-8">
<title>Brightledger Business Card</title>
<link rel="stylesheet" href="https://fonts.googleapis.com/css2?family=Lato:wght@400;700&family=Cormorant+Garamond:wght@500&display=swap">
<style>
  :root {
    --stage-dark: #222222;
    --stage-light: #4a4a4a;
    --card-white: #ffffff;
    --card-blue: #4569b3;
    --ink-blue: #1f3f99;
    --ink-brown: #8a6420;
    --gold: #b98a2e;
    --rule: #b8bde6;
  }
  * { margin: 0; padding: 0; box-sizing: border-box; }
  html, body { width: 1200px; height: 750px; overflow: hidden; }
  body {
    background: radial-gradient(ellipse at 50% 45%, var(--stage-light) 0%, var(--stage-dark) 75%);
    font-family: "Lato", sans-serif;
    position: relative;
  }
  .card {
    position: absolute;
    top: 186px;
    height: 328px;
    box-shadow: 0 4px 10px rgba(0,0,0,0.45);
    overflow: hidden;
  }
  .card-front { left: 38px; width: 559px; background: var(--card-white); }
  .card-back { left: 610px; width: 562px; background: var(--card-blue); }

  .brand {
    position: absolute;
    display: flex;
    align-items: center;
    gap: 10px;
    font-family: "Lato", sans-serif;
    font-weight: 700;
    color: var(--gold);
    white-space: nowrap;
  }
  .brand-mark { background: var(--gold); display: block; }
  .card-front .brand { left: 52px; top: 146px; font-size: 29px; }
  .card-front .brand-mark { width: 24px; height: 24px; }

  .divider {
    position: absolute;
    left: 278px; top: 62px;
    width: 3px; height: 202px;
    background: var(--rule);
  }
  .details { position: absolute; left: 304px; top: 56px; }
  .company-title {
    font-family: "Cormorant Garamond", serif;
    font-weight: 500;
    font-size: 28px;
    letter-spacing: 0.2px;
    color: var(--ink-brown);
    line-height: 1;
  }
  .company-title .lead { color: var(--ink-blue); }
  .address {
    margin-top: 20px;
    font-size: 16px;
    line-height: 23px;
    color: var(--ink-blue);
  }
  .contacts { list-style: none; margin-top: 19px; }
  .contacts li {
    display: flex; align-items: center;
    height: 22.3px;
    font-size: 16px;
    color: var(--ink-brown);
  }
  .contacts svg { width: 18px; height: 16px; margin-right: 12px; fill: var(--ink-blue); flex: none; }
  .services {
    position: absolute;
    left: 0; right: 0; top: 284px;
    text-align: center;
    font-size: 16px;
    color: var(--ink-brown);
    padding-right: 0;
  }

  .pentagon { position: absolute; left: 0; top: 0; }
  .card-back .brand {
    left: 0; right: 0; top: 140px;
    flex-direction: column; gap: 12px;
    font-size: 33px;
    color: #6e4b1b;
  }
  .card-back .brand-mark { width: 44px; height: 44px; background: #6e4b1b; }
</style>
</head>
<body>
  <section class="card card-front">
    <div class="brand"><span class="brand-mark"></span><span class="brand-name">Brightledger</span></div>
    <div class="divider"></div>
    <div class="details">
      <h1 class="company-title"><span class="lead">BR</span>IGHTLEDGER</h1>
      <p class="address">48276 9th Ave S Ste 305<br>Federal Way, WA 98117</p>
      <ul class="contacts">
        <li><svg viewBox="0 0 18 16" aria-hidden="true"><path d="M1 6c0-3 16-3 16 0v2h-4V6H5v2H1z"/><path d="M4 9h10l2 6H2z"/><circle cx="9" cy="12" r="1.6" fill="#fff"/></svg>(360)418-2096</li>
        <li><svg viewBox="0 0 18 16" aria-hidden="true"><path d="M5 0h8v16H5z M6.5 1.5v11h5v-11z"/><circle cx="9" cy="14.2" r="0.9"/></svg>(360)586-7319</li>
        <li><svg viewBox="0 0 18 16" aria-hidden="true"><path d="M4 0h10v5H4zM1 5h16v7h-3v4H4v-4H1z M5.5 9v5.5h7V9z"/></svg>(360)418-2157</li>
        <li><svg viewBox="0 0 18 16" aria-hidden="true"><path d="M0 3h18v11H0z"/><path d="M0.5 3.5l8.5 6 8.5-6M0.5 13.5l6-5M17.5 13.5l-6-5" stroke="#fff" stroke-width="1.2" fill="none"/></svg>brightledger@mailbox.com</li>
      </ul>
    </div>
    <p class="services">“Accounting” “Payroll” “Licenses” “Audits” “Tax .”</p>
  </section>

  <section class="card card-back">
    <svg class="pentagon" width="562" height="328" viewBox="0 0 562 328" aria-hidden="true">
      <polygon points="280,28 426,136 368,310 186,308 131,134" fill="#ffffff"/>
    </svg>
    <div class="brand"><span class="brand-mark"></span><span class="brand-name">Brightledger</span></div>
  </section>
</body>
</html>
```